Suds Harbor Laundromat Wordpress Design

We need a Wordpress website design for our laundromat, Suds Harbor Atlanta, at www.sudsharboratlanta-example.com. We would like to have 6 pages: Home, About Us, Services, Locations, Reviews and Contact us. We will provide content for the text on each page. What we do: We are a full service laundromat that provides dry cleaning drop off, professional laundry services, wash dry fold and self service laundry to the local community. We would like to use the color scheme from our logo to convey a warm, safe, and bright business that caters to its diverse community.
Updates

I like the structure of this laundromat website: http://www.tumblewashhub-example.com/ Using my logo and color scheme in the above referenced website is what. Am looking for. The photos attached to the project with the female model should be used as a primary focus and supplemented by actual photos of the equipment.

Target Market(s)

Our target market is a diverse group of people from Midtown Atlanta - LGBTQ community /Locals/Regulars that have been coming to laundromat for 30 years.

Industry/Entity Type

Laundromat

Coding

Coded - Design and coding required

Number of Pages Required

5+ page

Font styles to use
Sans Serif

Colors
0054AA
0677BA
7BADD7
CADEEF
E8F1F8

Requirements
Must have
• Feature this video on the main page: https://video.example.com/Qx7mBr2Lp0Z

```html
<!DOCTYPE html>
<html lang="en">
<head>
<meta charset="utf-8">
<title>Suds Harbor Atlanta</title>
<link href="https://fonts.googleapis.com/css2?family=Montserrat:wght@500;600;700;800&family=Open+Sans:wght@400;600;700&display=swap" rel="stylesheet">
<style>
:root{
  --navy:#0054AA;
  --blue:#0677BA;
  --sky:#7BADD7;
  --mist:#CADEEF;
  --ice:#E8F1F8;
  --page:#EAF3FA;
  --ink:#1d2b3a;
  --muted:#5b6b7c;
  --white:#ffffff;
  --star:#f4b324;
}
*{box-sizing:border-box;margin:0;padding:0}
html,body{width:1200px;height:3052px;overflow:hidden}
body{background:var(--page);font-family:"Open Sans",Arial,sans-serif;color:var(--ink);position:relative}
.abs{position:absolute}

/* header */
.site-header{position:absolute;top:0;left:0;width:1200px;height:62px;background:rgba(255,255,255,.95);z-index:5;display:flex;align-items:center;justify-content:space-between;padding:0 180px 0 150px}
.brand{display:flex;align-items:center;gap:10px;font-family:"Montserrat",sans-serif;font-weight:700;font-size:20px;color:var(--navy)}
.brand-dot{width:16px;height:16px;border-radius:50%;background:var(--blue)}
.main-nav{display:flex;gap:6px}
.main-nav a{font-size:12px;color:var(--ink);text-decoration:none;padding:8px 14px;font-weight:600}
.main-nav a.active{background:var(--ice);color:var(--blue);border-radius:3px}

/* hero */
.hero-photo{position:absolute;top:0;left:0;width:1200px;height:720px;background:linear-gradient(160deg,#9fb9d2 0%,#5f86ad 45%,#2f5d8c 100%)}
.hero-copy{position:absolute;top:256px;left:0;width:1200px;text-align:center;color:var(--white)}
.hero-badge{display:inline-block;background:var(--navy);font-size:13px;padding:5px 14px;border-radius:3px;font-weight:600}
.hero-title{font-family:"Montserrat",sans-serif;font-weight:800;font-size:48px;letter-spacing:1px;margin-top:14px;text-shadow:0 2px 8px rgba(0,0,0,.3)}
.hero-sub{font-family:"Montserrat",sans-serif;font-weight:500;font-size:22px;color:var(--ice);margin-top:4px}

/* what we do */
.video-frame{position:absolute;top:790px;left:180px;width:360px;height:180px;background:linear-gradient(120deg,#c23bd4,#5f3ad0 55%,#2a6fd0)}
.play-btn{position:absolute;left:163px;top:74px;width:40px;height:30px;background:#e03131;border-radius:8px}
.play-btn::after{content:"";position:absolute;left:16px;top:8px;border-left:12px solid #fff;border-top:7px solid transparent;border-bottom:7px solid transparent}
.about{position:absolute;top:796px;left:566px;width:440px}
.section-heading{font-family:"Montserrat",sans-serif;font-weight:700;font-size:30px;color:var(--ink)}
.section-heading .accent{color:var(--blue)}
.about p{font-size:12px;line-height:1.6;color:var(--muted);margin-top:8px}
.btn{display:inline-block;background:var(--navy);color:#fff;font-size:10px;font-weight:700;letter-spacing:.5px;padding:10px 20px;border-radius:3px;margin-top:16px;text-decoration:none}

/* services */
.services-photo{position:absolute;top:1110px;left:0;width:1200px;height:650px;background:linear-gradient(180deg,#2d69ad,#1d4f8f 60%,#2a63a6)}
.services-title{position:absolute;top:1258px;left:0;width:1200px;text-align:center;font-family:"Montserrat",sans-serif;font-weight:700;font-size:34px;color:#fff}
.service-list{position:absolute;top:1346px;left:176px;width:848px;display:flex;justify-content:space-between}
.service-card{width:148px;height:270px;background:var(--ice);border:3px solid #fff;border-radius:74px;text-align:center;padding-top:14px;position:relative;box-shadow:0 6px 16px rgba(0,0,0,.2)}
.service-card.featured{background:#fff;border-color:var(--navy)}
.service-icon{width:112px;height:112px;border-radius:50%;background:#fff;border:2px solid var(--mist);margin:0 auto;display:flex;align-items:center;justify-content:center}
.service-name{font-family:"Montserrat",sans-serif;font-weight:700;font-size:14px;color:var(--navy);margin-top:38px;line-height:1.3}
.card-arrow{position:absolute;left:57px;bottom:18px;width:28px;height:28px;border-radius:50%;background:var(--navy)}
.card-arrow::after{content:"";position:absolute;left:11px;top:8px;border-left:8px solid #fff;border-top:6px solid transparent;border-bottom:6px solid transparent}

/* reviews */
.reviews-title{position:absolute;top:1858px;left:0;width:1200px;text-align:center;font-family:"Montserrat",sans-serif;font-weight:700;font-size:34px}
.review-list{position:absolute;top:1985px;left:176px;width:848px;display:flex;justify-content:space-between}
.review-card{width:270px;height:190px;background:#fff;border:1px solid var(--mist);text-align:center;padding:44px 22px 0;position:relative}
.review-card.featured{border:3px solid var(--mist)}
.avatar{position:absolute;top:-26px;left:106px;width:56px;height:56px;border-radius:50%;background:linear-gradient(135deg,var(--sky),var(--blue));border:3px solid #fff}
.reviewer{font-weight:700;font-size:12px;color:var(--ink)}
.stars{color:var(--star);font-size:13px;letter-spacing:2px;margin-top:2px}
.review-text{font-size:10.5px;line-height:1.55;color:var(--muted);margin-top:8px}
.dots{position:absolute;top:2222px;left:0;width:1200px;display:flex;justify-content:center;gap:7px}
.dots span{width:8px;height:8px;border-radius:50%;background:var(--mist)}
.dots span.on{background:var(--navy)}

/* location */
.location-title{position:absolute;top:2462px;left:0;width:1200px;text-align:center;font-family:"Montserrat",sans-serif;font-weight:700;font-size:34px}
.map{position:absolute;top:2560px;left:180px;width:384px;height:238px;background:linear-gradient(135deg,#eef1ef,#dfe6e2 60%,#cfdcd6);border:1px solid var(--mist)}
.contact{position:absolute;top:2572px;left:810px;width:230px;font-size:11px;color:var(--muted);line-height:1.5}
.contact h3{font-family:"Montserrat",sans-serif;font-size:13px;color:var(--ink);font-weight:700;margin-bottom:8px}
.contact-row{display:flex;gap:10px;margin-bottom:10px}
.contact-row svg{flex:none;margin-top:2px}
.contact strong{color:var(--ink)}
.note{position:absolute;top:2802px;left:810px;width:210px;background:var(--ice);border:1px solid var(--mist);font-size:10px;line-height:1.5;color:var(--muted);padding:8px 10px}

/* footer */
.site-footer{position:absolute;top:2920px;left:0;width:1200px;height:132px;background:var(--navy);color:#fff;text-align:center}
.footer-nav{display:flex;justify-content:center;gap:38px;padding-top:24px;font-size:12px;font-weight:600}
.socials{display:flex;justify-content:center;gap:12px;margin-top:16px}
.socials span{width:24px;height:24px;border-radius:50%;background:#fff;opacity:.9}
.copyright{position:absolute;left:40px;bottom:12px;font-size:10px;color:var(--mist)}
</style>
</head>
<body>

<header class="site-header">
  <div class="brand"><span class="brand-dot"></span>Suds Harbor</div>
  <nav class="main-nav">
    <a class="active" href="#">Home</a><a href="#">About Us</a><a href="#">Services</a><a href="#">Locations</a><a href="#">Reviews</a><a href="#">Contact us</a>
  </nav>
</header>

<div class="hero-photo" role="img" aria-label="Model seated in front of a row of front-loading washing machines in the laundromat"></div>
<div class="hero-copy">
  <span class="hero-badge">In business over 30 years</span>
  <h1 class="hero-title">SUDS HARBOR</h1>
  <p class="hero-sub">Coin Laundry, Dry Cleaning, &amp; Professional Laundry</p>
</div>
<svg class="abs" style="top:560px;left:0" width="1200" height="170" viewBox="0 0 1200 170">
  <path d="M0 90 C300 160 600 40 900 70 C1020 82 1120 120 1200 100 L1200 170 L0 170Z" fill="var(--page)"/>
  <path d="M0 80 C300 150 600 30 900 60 C1020 72 1120 110 1200 90" fill="none" stroke="var(--navy)" stroke-width="6"/>
  <path d="M0 100 C300 165 600 50 900 80 C1020 92 1120 128 1200 110" fill="none" stroke="var(--sky)" stroke-width="3"/>
</svg>

<div class="video-frame" role="img" aria-label="Featured brand video thumbnail with the model in colorful light">
  <span class="play-btn"></span>
</div>
<section class="about">
  <h2 class="section-heading"><span class="accent">What</span> we do</h2>
  <p>We are a full service laundromat that provides dry cleaning drop off, professional laundry services, wash dry fold and self service laundry to the local community. We would like to use the color scheme from our logo to convey a warm, safe, and bright business that caters to its diverse community.</p>
  <a class="btn" href="#">LEARN MORE</a>
</section>

<div class="services-photo" role="img" aria-label="Laundromat interior with rows of washers, tinted blue"></div>
<svg class="abs" style="top:1080px;left:0" width="1200" height="120" viewBox="0 0 1200 120">
  <path d="M0 0 L1200 0 L1200 40 C950 110 700 20 450 60 C280 88 120 90 0 60Z" fill="var(--page)"/>
  <path d="M0 60 C120 90 280 88 450 60 C700 20 950 110 1200 40" fill="none" stroke="var(--navy)" stroke-width="6"/>
  <path d="M0 76 C120 104 280 102 450 76 C700 36 950 124 1200 56" fill="none" stroke="var(--sky)" stroke-width="3"/>
</svg>
<h2 class="services-title">Our Services</h2>
<div class="service-list">
  <div class="service-card">
    <div class="service-icon"><svg width="56" height="56" viewBox="0 0 56 56" fill="none" stroke="var(--navy)" stroke-width="3"><path d="M20 8 L8 16 L12 26 L16 24 L16 48 L40 48 L40 24 L44 26 L48 16 L36 8 C34 14 22 14 20 8Z"/></svg></div>
    <div class="service-name">Dry Clean<br>Service</div>
  </div>
  <div class="service-card">
    <div class="service-icon"><svg width="56" height="56" viewBox="0 0 56 56" fill="none" stroke="var(--navy)" stroke-width="3"><path d="M18 8 L10 18 L10 50 L46 50 L46 18 L38 8 L28 20Z M28 20 L28 50"/></svg></div>
    <div class="service-name">Leather &amp; Suede<br>Service</div>
  </div>
  <div class="service-card featured">
    <div class="service-icon"><svg width="56" height="56" viewBox="0 0 56 56" fill="none" stroke="var(--navy)" stroke-width="3"><rect x="10" y="6" width="36" height="44" rx="3"/><line x1="10" y1="16" x2="46" y2="16"/><circle cx="28" cy="33" r="10"/></svg></div>
    <div class="service-name">Wash,Dry,Fold<br>Service</div>
    <span class="card-arrow"></span>
  </div>
  <div class="service-card">
    <div class="service-icon"><svg width="60" height="56" viewBox="0 0 60 56" fill="none" stroke="var(--navy)" stroke-width="3"><rect x="4" y="18" width="16" height="30"/><rect x="22" y="18" width="16" height="30"/><rect x="40" y="18" width="16" height="30"/><circle cx="12" cy="36" r="5"/><circle cx="30" cy="36" r="5"/><circle cx="48" cy="36" r="5"/></svg></div>
    <div class="service-name">Oversize<br>Machines</div>
  </div>
  <div class="service-card">
    <div class="service-icon"><svg width="56" height="56" viewBox="0 0 56 56" fill="none" stroke="var(--navy)" stroke-width="3"><rect x="12" y="6" width="32" height="44" rx="2"/><line x1="18" y1="16" x2="38" y2="16"/><line x1="18" y1="24" x2="38" y2="24"/><line x1="18" y1="32" x2="30" y2="32"/><path d="M30 42 L34 46 L42 36"/></svg></div>
    <div class="service-name">Commercial<br>Accounts</div>
  </div>
</div>
<svg class="abs" style="top:1670px;left:0" width="1200" height="130" viewBox="0 0 1200 130">
  <path d="M0 50 C250 110 500 10 800 50 C950 70 1080 100 1200 70 L1200 130 L0 130Z" fill="var(--page)"/>
  <path d="M0 50 C250 110 500 10 800 50 C950 70 1080 100 1200 70" fill="none" stroke="var(--navy)" stroke-width="6"/>
  <path d="M0 66 C250 126 500 26 800 66 C950 86 1080 116 1200 86" fill="none" stroke="var(--sky)" stroke-width="3"/>
</svg>

<h2 class="reviews-title">Reviews</h2>
<div class="review-list">
  <article class="review-card">
    <span class="avatar" role="img" aria-label="Reviewer portrait"></span>
    <div class="reviewer">Marla</div>
    <div class="stars">★★★★★</div>
    <p class="review-text">Friendly staff, spotless machines and my clothes always come back folded perfectly. This has been my go-to laundromat for years and I love the warm vibe.</p>
  </article>
  <article class="review-card featured">
    <span class="avatar" role="img" aria-label="Reviewer portrait"></span>
    <div class="reviewer">Devon</div>
    <div class="stars">★★★★★</div>
    <p class="review-text">Dropped off a big load of bedding and it was ready the same day. Great prices, clean space, and the team really cares about the neighborhood.</p>
  </article>
  <article class="review-card">
    <span class="avatar" role="img" aria-label="Reviewer portrait"></span>
    <div class="reviewer">Eli</div>
    <div class="stars">★★★★★</div>
    <p class="review-text">Their dry cleaning is excellent and my suede jacket looks brand new. Easy parking, plenty of machines and always a welcoming smile.</p>
  </article>
</div>
<div class="dots"><span class="on"></span><span></span><span></span></div>

<svg class="abs" style="top:2290px;left:0" width="1200" height="140" viewBox="0 0 1200 140">
  <path d="M0 110 C200 40 420 40 640 80 C860 120 1040 90 1200 40" fill="none" stroke="var(--navy)" stroke-width="7"/>
  <path d="M0 124 C200 56 420 56 640 96 C860 136 1040 106 1200 56" fill="none" stroke="var(--sky)" stroke-width="3"/>
</svg>

<h2 class="location-title">Location</h2>
<div class="map" role="img" aria-label="Street map showing the laundromat location in Midtown Atlanta"></div>
<div class="contact">
  <h3>Address</h3>
  <div class="contact-row">
    <svg width="12" height="14" viewBox="0 0 12 14"><path d="M6 0C2.7 0 0 2.6 0 5.8 0 10 6 14 6 14s6-4 6-8.2C12 2.6 9.3 0 6 0z" fill="var(--navy)"/><circle cx="6" cy="5.6" r="2" fill="#fff"/></svg>
    <div><strong>Suds Harbor Atlanta</strong><br>1480 Harbor Mill Rd NE, Atlanta, GA 30300<br>United States</div>
  </div>
  <div class="contact-row">
    <svg width="12" height="12" viewBox="0 0 12 12"><path d="M2.5 0.5 L4.5 3 L3.3 4.6 C4 6.2 5.8 8 7.4 8.7 L9 7.5 L11.5 9.5 L10 11.5 C5 11 1 7 0.5 2Z" fill="var(--navy)"/></svg>
    <div>404-555-0142 &nbsp;<strong>Contact Us</strong></div>
  </div>
  <div class="contact-row">
    <svg width="12" height="12" viewBox="0 0 12 12"><circle cx="6" cy="6" r="5" fill="none" stroke="var(--navy)" stroke-width="1.6"/><path d="M6 3V6.3L8 7.5" stroke="var(--navy)" stroke-width="1.4" fill="none"/></svg>
    <div><strong>Open Hours</strong><br>7 Days a week<br>8am to 8pm<br>Last Wash Begins 6:30pm</div>
  </div>
</div>
<p class="note">Located conveniently in Midtown next to the Corner Market in the Harbor Square Shopping Center.</p>

<footer class="site-footer">
  <nav class="footer-nav"><span>Home</span><span>About Us</span><span>Services</span><span>Locations</span><span>Reviews</span><span>Contact us</span></nav>
  <div class="socials"><span></span><span></span></div>
  <p class="copyright">© Suds Harbor Atlanta. All rights reserved. www.sudsharboratlanta-example.com</p>
</footer>

</body>
</html>
```